Church needs a street sign design

We're a small church located in Silicon Valley, California. Our website is https://www.hpkwendell.org/ and our address is 1847 Thornby Ave, San Jose, California, 95871. You can look up our location on Google Maps to see the sign from Street View. I have uploaded an image of the street sign as well. The marquee, the top section of the sign, and the separating line between them both will be removed. We're seeking a design for a new backlit acrylic insert that will go on the front of the light box and the back of the lightbox. The acrylic sign will fill the entire external frame. In the future, we may build a decorative wood frame around the structural legs, as visualized in one of the uploaded files. The church's brand colors are: #003366 (dark blue), #ff6600 (vibrant orange), #228b22 (forest green). I have also uploaded the church's logo assets. Our primary font is Montserrat and the secondary is Poppins. You can deviate from these colors/fonts if the sign is still coherent with the rest of our branding. Our branding values are mission, truth, passion, and community (please do not put those words on the sign! They are just intended to guide the look of the design). The sign dimensions are 96" by 47.5". Keep in mind that the sign will be backlit on a busy street side. It will also be positioned next to an old-looking church building. We do NOT want a sign that looks traditional, old, or antiquated. Instead, we want a modern-looking sign that pairs well with our old building while helping it look more modern too. We would also like the web address clearly visible on the sign: hpkwendell.org. If you have any questions, just let me know!

```html
<!DOCTYPE html>
<html lang="en">
<head>
<meta charset="utf-8">
<title>Wendell Community Church – Street Sign</title>
<link rel="stylesheet" href="https://fonts.googleapis.com/css2?family=Montserrat:wght@700&family=Poppins:wght@500&display=swap">
<style>
  :root {
    --navy: #0f2563;
    --panel-white: #eef0f4;
    --mark-grey: #dfe3ea;
    --orange: #e65c10;
    --white: #ffffff;
    --backdrop: #e9e9ec;
  }
  html, body {
    margin: 0;
    width: 1200px;
    height: 2562px;
    overflow: hidden;
    background: var(--backdrop);
  }
  .street-sign {
    position: absolute;
    left: 50px;
    top: 1009px;
    width: 1100px;
    height: 544px;
    background: var(--navy);
    overflow: hidden;
  }
  .brand-square {
    position: absolute;
    left: 110px;
    top: 150px;
    width: 190px;
    height: 190px;
    background: var(--mark-grey);
  }
  .name-band {
    position: absolute;
    left: 440px;
    top: 148px;
    width: 660px;
    height: 154px;
    background: var(--panel-white);
  }
  .church-name {
    position: absolute;
    left: 498px;
    top: 150px;
    margin: 0;
    font-family: "Montserrat", sans-serif;
    font-weight: 700;
    color: var(--navy);
    line-height: 1;
  }
  .church-name .name-main {
    display: block;
    font-size: 96px;
    letter-spacing: -1px;
  }
  .church-name .name-sub {
    display: block;
    margin-top: 6px;
    font-size: 33px;
    letter-spacing: 0.5px;
  }
  .location-pin {
    position: absolute;
    left: 669px;
    top: 313px;
    width: 70px;
    height: 70px;
  }
  .address {
    position: absolute;
    left: 440px;
    width: 528px;
    top: 388px;
    margin: 0;
    text-align: center;
    font-family: "Poppins", sans-serif;
    font-weight: 500;
    font-size: 30px;
    line-height: 38px;
    letter-spacing: 3px;
    color: var(--white);
  }
  .web-band {
    position: absolute;
    left: 0;
    bottom: 0;
    width: 100%;
    height: 62px;
    background: var(--orange);
    display: flex;
    align-items: center;
    justify-content: center;
  }
  .web-address {
    font-family: "Poppins", sans-serif;
    font-weight: 500;
    font-size: 21px;
    letter-spacing: 0.95em;
    color: var(--white);
    text-transform: uppercase;
  }
</style>
</head>
<body>
  <div class="street-sign">
    <div class="brand-square"></div>
    <div class="name-band"></div>
    <h1 class="church-name">
      <span class="name-main">WENDELL</span>
      <span class="name-sub">COMMUNITY CHURCH</span>
    </h1>
    <svg class="location-pin" viewBox="0 0 70 70" aria-hidden="true">
      <circle cx="35" cy="35" r="35" fill="var(--orange)"/>
      <path d="M35 16c-8 0-13.5 5.8-13.5 13 0 9 13.5 22 13.5 22s13.5-13 13.5-22c0-7.2-5.5-13-13.5-13z" fill="none" stroke="var(--white)" stroke-width="4"/>
      <circle cx="35" cy="29" r="4.5" fill="var(--white)"/>
    </svg>
    <p class="address">1847 Thornby Ave, San Jose<br>California, 95871</p>
    <div class="web-band">
      <span class="web-address">www.hpkwendell.org</span>
    </div>
  </div>
</body>
</html>
```